Brivola website blog. Simple medical advice given in clear yes or no answers that save people money

I am developing a new web page that provides medical care cost savings at the consumers' fingertips. I need a web page that is clean, concise, and attractive for me to put my valuable medical information on. The information I provide is simple to obtain, yet very valuable to the consumer, and answered in a yes or no format. For example, A person may wonder if they need an antibiotic for cold like symptoms. Seeing a doctor for an antibiotic is very expensive. But with simple and clear advice at their fingertips, they can confidently avoid having to pay $200 or more to see a doctor and get an antibiotic. This is kind of like tallwick digest for medical services.

Target Market(s)

People who are savvy shoppers and want to save money on healthcare. Likely younger ages between 21 and 60, who are mobile, readily use kelvexes, and want strong evidence based research to guide their decisions.

Industry/Entity Type

Lifestyle

Coding

Coded - Design and coding required

Number of Pages Required

5+ page

Colors

Designer to choose colors to be used in the design.

Requirements
Must have
• A template on the "Question" and "Answer" page that can be edited many times that can be edited many times. The Confidence rating scale would need to be edited as well. The "Date Researched" the "Brivola Brivogram" and "References" all need to be able to be edited. This website must be very clear and simple to understand. A medical question is posed with a yes or no answer, then answered and given a confidence rating, we then tell them how much money they saved by going to our website.
Nice to have
• We want this to be slightly fun, vibrant, warm and inviting. This will be sometime later converted into an app format. Quirky, some humor to keep it interesting.
Should not have
• No sterile looking medical images. Not boring.

```html
<!DOCTYPE html>
<html lang="en">
<head>
<meta charset="utf-8">
<title>Brivola — Clear Valuable Health Advice Right Now</title>
<link href="https://fonts.googleapis.com/css2?family=Open+Sans:wght@300;400;600;700&display=swap" rel="stylesheet">
<style>
  :root {
    --white: #ffffff;
    --brand-red: #d8232a;
    --brand-blue: #1565b8;
    --nav-blue: #1668bd;
    --nav-active: #0f4f93;
    --title-grey: #6b6b6b;
    --sidebar-bg: #2a2a2a;
    --sidebar-line: #3d3d3d;
    --sidebar-text: #b5b5b5;
    --footer-left: #202020;
    --footer-right: #2c2c2c;
    --footer-text: #a9a9a9;
    --field-bg: #e6e6e6;
    --field-text: #444444;
    --hero-deep: #3b6d9c;
    --hero-mid: #8fb6d8;
    --hero-light: #d9e8f4;
    --hero-warm: #e9c9b0;
  }
  * { box-sizing: border-box; margin: 0; padding: 0; }
  html, body { width: 1200px; height: 718px; overflow: hidden; }
  body { font-family: "Open Sans", Arial, sans-serif; background: var(--white); position: relative; }

  .site-header { position: absolute; left: 0; top: 0; width: 1200px; height: 113px; background: var(--white); }
  .brand { position: absolute; left: 144px; top: 40px; display: flex; align-items: center; gap: 10px; }
  .brand-dot { width: 26px; height: 26px; border-radius: 50%; background: var(--brand-blue); }
  .brand-name { font-size: 28px; font-weight: 600; color: var(--brand-blue); letter-spacing: 0.5px; }
  .tagline { position: absolute; right: 146px; top: 30px; font-size: 35px; font-weight: 300; color: var(--title-grey); letter-spacing: 0.2px; }

  .main-nav { position: absolute; left: 0; top: 113px; width: 1200px; height: 40px; background: var(--nav-blue); }
  .main-nav ul { list-style: none; display: flex; position: absolute; left: 143px; top: 0; height: 40px; }
  .main-nav li { height: 40px; line-height: 40px; font-size: 13.6px; color: var(--white); }
  .main-nav li.active { background: var(--nav-active); }

  .side-menu { position: absolute; left: 0; top: 153px; width: 400px; height: 405px; background: var(--sidebar-bg); }
  .side-menu ul { list-style: none; position: absolute; left: 122px; top: 0; width: 278px; }
  .side-menu li { height: 56px; border-bottom: 1px solid var(--sidebar-line); display: flex; align-items: center; padding-left: 22px; font-size: 16.5px; color: var(--sidebar-text); }
  .side-menu li:last-child { border-bottom: none; }
  .side-menu li.current { color: var(--white); }
  .side-menu .bullet { width: 11px; height: 11px; margin-right: 10px; flex: none; }

  .hero { position: absolute; left: 400px; top: 153px; width: 800px; height: 405px; overflow: hidden; }
  .hero-art { position: absolute; inset: 0;
    background:
      radial-gradient(circle at 186px 210px, #fff4ea 0, var(--hero-warm) 30px, rgba(233,201,176,0) 110px),
      radial-gradient(ellipse at 200px 250px, rgba(230,230,235,0.8) 0, rgba(230,230,235,0) 260px),
      linear-gradient(100deg, var(--hero-deep) 0%, var(--hero-mid) 45%, var(--hero-light) 70%, var(--hero-mid) 100%); }
  .search-box { position: absolute; left: 410px; top: 24px; width: 246px; height: 40px; background: rgba(235,240,245,0.95); display: flex; align-items: center; justify-content: space-between; padding: 0 14px 0 15px; font-size: 12.5px; color: var(--field-text); }
  .callout { position: absolute; left: 410px; top: 152px; width: 246px; height: 101px; background: rgba(255,255,255,0.93); padding: 14px 11px 0 0; text-align: right; font-size: 16.5px; line-height: 24px; color: #222; }
  .slide-arrow { position: absolute; top: 187px; width: 25px; height: 32px; background: rgba(40,40,40,0.55); display: flex; align-items: center; justify-content: center; }
  .slide-arrow.prev { left: 0; }
  .slide-arrow.next { right: 0; }

  .footer { position: absolute; left: 0; top: 558px; width: 1200px; height: 160px; }
  .footer-left { position: absolute; left: 0; top: 0; width: 400px; height: 160px; background: var(--footer-left); }
  .footer-right { position: absolute; left: 400px; top: 0; width: 800px; height: 160px; background: var(--footer-right); }
  .copyright { position: absolute; left: 143px; top: 30px; font-size: 12px; line-height: 26px; color: var(--footer-text); }
  .social { position: absolute; left: 144px; top: 114px; display: flex; gap: 14px; }
  .social span { width: 14px; height: 14px; border-radius: 50%; background: #8a8a8a; }
  .disclaimer { position: absolute; left: 23px; top: 32px; width: 390px; }
  .disclaimer h3 { font-size: 12px; font-weight: 400; color: var(--white); margin-bottom: 4px; }
  .disclaimer p { font-size: 8.8px; line-height: 16px; color: #9a9a9a; }
  .signup { position: absolute; right: 144px; top: 28px; width: 216px; text-align: right; }
  .signup h3 { font-size: 17px; font-weight: 400; color: var(--white); margin-bottom: 7px; }
  .email-field { height: 36px; background: var(--field-bg); display: flex; align-items: center; justify-content: space-between; padding: 0 12px 0 15px; font-size: 12px; color: var(--field-text); text-align: left; }
  .signup .ask { font-size: 12px; color: var(--footer-text); margin-top: 9px; }
  .signup .post { font-size: 13.5px; font-weight: 600; color: var(--white); margin-top: 2px; }
</style>
</head>
<body>
  <header class="site-header">
    <div class="brand"><span class="brand-dot"></span><span class="brand-name">Brivola</span></div>
    <h1 class="tagline">Clear Valuable Health Advice Right Now</h1>
  </header>

  <nav class="main-nav">
    <ul>
      <li class="active" style="padding:0 29px;">Prev/Screening</li>
      <li style="padding:0 25px 0 24px;">Women’s Health</li>
      <li style="padding:0 25px 0 25px;">Men’s Health</li>
      <li style="padding:0 25px 0 25px;">Meds</li>
      <li style="padding:0 25px 0 25px;">Surgery</li>
      <li style="padding:0 25px 0 25px;">Imaging</li>
      <li style="padding:0 25px 0 25px;">Peds</li>
      <li style="padding:0 25px 0 25px;">Condimentum</li>
    </ul>
  </nav>

  <aside class="side-menu">
    <ul>
      <li class="current"><svg class="bullet" viewBox="0 0 12 12"><circle cx="6" cy="6" r="6" fill="currentColor"/><path d="M5 3.5 7.5 6 5 8.5" stroke="#2a2a2a" stroke-width="1.6" fill="none"/></svg>Who Are We?</li>
      <li><svg class="bullet" viewBox="0 0 12 12"><circle cx="6" cy="6" r="6" fill="currentColor"/><path d="M5 3.5 7.5 6 5 8.5" stroke="#2a2a2a" stroke-width="1.6" fill="none"/></svg>How It Works</li>
      <li><svg class="bullet" viewBox="0 0 12 12"><circle cx="6" cy="6" r="6" fill="currentColor"/><path d="M5 3.5 7.5 6 5 8.5" stroke="#2a2a2a" stroke-width="1.6" fill="none"/></svg>How We Know</li>
      <li><svg class="bullet" viewBox="0 0 12 12"><circle cx="6" cy="6" r="6" fill="currentColor"/><path d="M5 3.5 7.5 6 5 8.5" stroke="#2a2a2a" stroke-width="1.6" fill="none"/></svg>Evidence Based Research</li>
      <li><svg class="bullet" viewBox="0 0 12 12"><circle cx="6" cy="6" r="6" fill="currentColor"/><path d="M5 3.5 7.5 6 5 8.5" stroke="#2a2a2a" stroke-width="1.6" fill="none"/></svg>Dr. Marlowe</li>
      <li><svg class="bullet" viewBox="0 0 12 12"><circle cx="6" cy="6" r="6" fill="currentColor"/><path d="M5 3.5 7.5 6 5 8.5" stroke="#2a2a2a" stroke-width="1.6" fill="none"/></svg>Who We Are Not</li>
      <li><svg class="bullet" viewBox="0 0 12 12"><circle cx="6" cy="6" r="6" fill="currentColor"/><path d="M5 3.5 7.5 6 5 8.5" stroke="#2a2a2a" stroke-width="1.6" fill="none"/></svg>Are We Biased?</li>
    </ul>
  </aside>

  <section class="hero">
    <div class="hero-art" role="img" aria-label="Doctor touching a glowing network of medical icons on a soft blue clinic background"></div>
    <div class="search-box">
      <span>Search</span>
      <svg width="15" height="15" viewBox="0 0 16 16"><circle cx="6.5" cy="6.5" r="5" stroke="#1668bd" stroke-width="2.2" fill="none"/><path d="M10.2 10.2 14.5 14.5" stroke="#1668bd" stroke-width="2.4" stroke-linecap="round"/></svg>
    </div>
    <div class="callout">Don’t Spend another clinic<br>on your health before<br>checking us out! It’s Free!</div>
    <div class="slide-arrow prev"><svg width="10" height="18" viewBox="0 0 10 18"><path d="M8 1 1.5 9 8 17" stroke="#fff" stroke-width="1.4" fill="none"/></svg></div>
    <div class="slide-arrow next"><svg width="10" height="18" viewBox="0 0 10 18"><path d="M2 1 8.5 9 2 17" stroke="#fff" stroke-width="1.4" fill="none"/></svg></div>
  </section>

  <footer class="footer">
    <div class="footer-left">
      <p class="copyright">Copyright &nbsp;©&nbsp; 2018 &nbsp;Brivola.<br>All rights reserved.</p>
      <div class="social" aria-label="Social links"><span></span><span></span><span></span></div>
    </div>
    <div class="footer-right">
      <div class="disclaimer">
        <h3>Disclaimer</h3>
        <p>Quisque aliquet ex nec est vestibulum pulvinar. Pellentesque convallis molestie enim sit amet efficitur. Etiam id imperdiet lectus. Vivamus lacus justo, ultrices nec erat in, euismod iaculis mauris. Vivamus eleifend vitae nulla vel malesuada. In ac malesuada lacus, et consectetur ante. Fusce vitae lectus sit amet mi pulvinar maximus. Aenean placerat, nibh vel accumsan aliquet, magna nibh accumsan nibh, ac tempus nunc ipsum ac tellus.</p>
      </div>
      <div class="signup">
        <h3>Become a Brivola Today!</h3>
        <div class="email-field">
          <span>Email Address</span>
          <svg width="14" height="11" viewBox="0 0 14 11"><rect x="0" y="0" width="14" height="11" rx="1" fill="#333"/><path d="M1 1.5 7 6 13 1.5" stroke="#e6e6e6" stroke-width="1.3" fill="none"/></svg>
        </div>
        <p class="ask">Ask a question here! If it is worthy</p>
        <p class="post">WE’LL POST IT!</p>
      </div>
    </div>
  </footer>
</body>
</html>
```